Entry Sign for Kelvastrom Champion Racing Kennel

Need main entrance sign design for sled dog racing and tourism company. Not a busy street, so doesn't need to catch attention. Thousands of guests will take picture by sign though, so more of a landmark than advertisement. Area is flood zone, so sign must be suspended off the ground between two large (80' tall) spruce trees about 10' apart. Area is spruce forest rain forest and gravel roads. Sign can be 8-10' long, and up to 10' high.

Target Market(s)

Tourists in Alaska

Industry/Entity Type

It Company

Font styles to use
Sans Serif

Requirements
Must have
• Must include logo elements, but don't have to be in same elongated shape. i.e. three dogs silhouette can me moved around. Must include material suggestions - potentially log, other wood, aluminum, or other rustic/natural looking material. Should also say (2004 & 2013) Kelvastrom Champion racing kennel, or something to that effect. see www.pelunova-example.com for more info.
Nice to have
• Ability to add/remove smaller signage below main sign, as our offerings and exploits change. See sample copperleaf lodge sign below. Small signs around location are home made using national park style signs. Racing team colors are red/yellow/black, but natural area and buildings are forest green and cedar colored wood. Any bold colors should be used sparingly.
Should not have
• no lighted or electric elements
• not anchored to ground

```html
<!DOCTYPE html>
<html lang="en">
<head>
<meta charset="utf-8">
<title>Kelvastrom Champion Racing Kennel – Entry Sign</title>
<link href="https://fonts.googleapis.com/css2?family=Kaushan+Script&family=Oswald:wght@700&family=Roboto+Slab:wght@800&family=Roboto:wght@400&display=swap" rel="stylesheet">
<style>
  :root {
    --backdrop: #eceee8;
    --wood-light: #e7b458;
    --wood-mid: #d89f3e;
    --wood-dark: #b57e26;
    --wood-edge: #9a6618;
    --ink: #2e1f08;
    --ink-soft: #5a3d12;
    --steel: #b9bcbe;
    --steel-dark: #6f7375;
    --badge: #ffffff;
  }
  html, body { margin: 0; padding: 0; overflow: hidden; }
  body { width: 1200px; height: 1200px; background: var(--backdrop); }
  .canvas { position: relative; width: 1200px; height: 1200px; overflow: hidden; }
  .sign-art { position: absolute; inset: 0; }

  .main-board-text {
    position: absolute; left: 215px; top: 290px; width: 620px; height: 420px;
    transform: rotate(-4deg); transform-origin: 50% 50%;
    font-family: "Kaushan Script", cursive; color: var(--ink);
    text-align: center;
  }
  .main-board-text > div { position: absolute; left: 0; width: 100%; line-height: 1; white-space: nowrap; }
  .kennel-mark { top: 48px; font-size: 34px; }
  .years { top: 132px; font-size: 62px; }
  .title { top: 220px; font-size: 58px; color: var(--ink-soft); }
  .subtitle { top: 292px; font-size: 64px; color: var(--ink-soft); }

  .offer-board-text {
    position: absolute; left: 355px; top: 745px; width: 325px; height: 190px;
    transform: rotate(-4deg); transform-origin: 50% 50%;
    color: var(--ink);
  }
  .offer-row { position: absolute; top: 52px; left: 28px; right: 28px; display: flex; align-items: center; justify-content: space-between; }
  .brand { font-family: "Roboto Slab", sans-serif; font-weight: 800; font-size: 16px; line-height: 1; white-space: nowrap; }
  .brand small { display: block; font-family: "Roboto", sans-serif; font-weight: 400; font-size: 7px; letter-spacing: .2px; margin-top: 3px; }
  .brand-dot { width: 30px; height: 30px; border-radius: 50%; background: var(--badge); }
  .phone { position: absolute; top: 105px; width: 100%; text-align: center; font-family: "Oswald", sans-serif; font-weight: 700; font-size: 44px; line-height: 1; letter-spacing: 1px; white-space: nowrap; }
</style>
</head>
<body>
<main class="canvas">
  <svg class="sign-art" width="1200" height="1200" viewBox="0 0 1200 1200" aria-hidden="true">
    <defs>
      <pattern id="chain-links" width="22" height="30" patternUnits="userSpaceOnUse">
        <ellipse cx="11" cy="15" rx="6" ry="12" fill="none" stroke="var(--steel)" stroke-width="4"/>
      </pattern>
      <linearGradient id="wood" x1="0" y1="0" x2="1" y2="1">
        <stop offset="0" stop-color="var(--wood-light)"/>
        <stop offset=".55" stop-color="var(--wood-mid)"/>
        <stop offset="1" stop-color="var(--wood-dark)"/>
      </linearGradient>
    </defs>

    <rect class="chain" x="376" y="40" width="22" height="270" fill="url(#chain-links)"/>
    <rect class="chain" x="630" y="20" width="22" height="270" fill="url(#chain-links)"/>
    <rect class="chain" x="440" y="690" width="22" height="100" fill="url(#chain-links)"/>
    <rect class="chain" x="573" y="680" width="22" height="100" fill="url(#chain-links)"/>
    <rect class="chain" x="438" y="920" width="22" height="60" fill="url(#chain-links)"/>
    <rect class="chain" x="574" y="905" width="22" height="60" fill="url(#chain-links)"/>

    <g class="main-board" transform="translate(215 290) rotate(-4 310 210)">
      <path d="M90 40 L530 40 Q540 70 570 75 L570 120 Q625 150 625 210 Q625 270 570 300 L570 345 Q540 350 530 380 L90 380 Q80 350 50 345 L50 300 Q-5 270 -5 210 Q-5 150 50 120 L50 75 Q80 70 90 40 Z"
            fill="var(--wood-edge)" transform="translate(4 10)"/>
      <path d="M90 40 L530 40 Q540 70 570 75 L570 120 Q625 150 625 210 Q625 270 570 300 L570 345 Q540 350 530 380 L90 380 Q80 350 50 345 L50 300 Q-5 270 -5 210 Q-5 150 50 120 L50 75 Q80 70 90 40 Z"
            fill="url(#wood)"/>
      <rect x="150" y="32" width="40" height="8" rx="2" fill="var(--steel-dark)"/>
      <rect x="410" y="32" width="40" height="8" rx="2" fill="var(--steel-dark)"/>
      <circle cx="30" cy="225" r="15" fill="var(--steel)" stroke="var(--steel-dark)" stroke-width="3"/>
      <circle cx="590" cy="210" r="15" fill="var(--steel)" stroke="var(--steel-dark)" stroke-width="3"/>
    </g>

    <g class="offer-board" transform="translate(355 745) rotate(-4 162 95)">
      <path d="M40 20 L110 20 Q115 32 125 32 Q135 32 140 20 L190 20 Q195 32 205 32 Q215 32 220 20 L285 20 Q325 30 325 95 Q325 160 285 170 L230 170 Q225 158 215 158 Q205 158 200 170 L115 170 Q110 158 100 158 Q90 158 85 170 L40 170 Q0 160 0 95 Q0 30 40 20 Z"
            fill="var(--wood-edge)" transform="translate(3 8)"/>
      <path d="M40 20 L110 20 Q115 32 125 32 Q135 32 140 20 L190 20 Q195 32 205 32 Q215 32 220 20 L285 20 Q325 30 325 95 Q325 160 285 170 L230 170 Q225 158 215 158 Q205 158 200 170 L115 170 Q110 158 100 158 Q90 158 85 170 L40 170 Q0 160 0 95 Q0 30 40 20 Z"
            fill="url(#wood)"/>
      <circle cx="14" cy="100" r="7" fill="var(--steel)" stroke="var(--steel-dark)" stroke-width="2"/>
      <circle cx="312" cy="90" r="7" fill="var(--steel)" stroke="var(--steel-dark)" stroke-width="2"/>
    </g>
  </svg>

  <div class="main-board-text">
    <div class="kennel-mark">Brannock's</div>
    <div class="years">(2004 &amp; 2013)</div>
    <div class="title">Kelvastrom Champion</div>
    <div class="subtitle">racing kennel</div>
  </div>

  <div class="offer-board-text">
    <div class="offer-row">
      <div class="brand">BRANNOCK'S<small>KELVASTROM RACING TEAM</small></div>
      <div class="brand-dot"></div>
      <div class="brand">PELUNOVA<small>SLED DOG TOURS</small></div>
    </div>
    <div class="phone">907-555-0142</div>
  </div>
</main>
</body>
</html>
```